Bref créative
Solo Practice Attorney Biz Cards & Stationery
Biz Cards and Stationery for Solo Practice
Professional
Thomas R. Halvorsen
Attorney At Law
Two Cedar Court
247 N.W. Ninth Street, Suite 2306
Fort Lauderdale, FL 33271
thomas@halvorsenlegalgroup.com
www.halvorsenlegalgroup.com
I would like to see several different ideas for business cards, stationery, and the like. I believe my logo reflects a professional, modern, yet modest character. I would like my other project materials to do the same. I will comment and offer suggestions as the project continues. Many thanks.
Ok, designers: I would like to put a QR Code on the back of the business card that links directly to my website. Does anyone have experience with this? Let me see what you can do.

```html
<!DOCTYPE html>
<html lang="en">
<head>
<meta charset="utf-8">
<title>Halvorsen Legal Group — Stationery Set</title>
<link rel="stylesheet" href="https://fonts.googleapis.com/css2?family=Cormorant+Garamond:wght@600&family=Lato:wght@300;400;700&display=swap">
<style>
:root{
  --navy:#1c3f7a;
  --navy-deep:#14305f;
  --ink:#222831;
  --muted:#6b7078;
  --paper:#ffffff;
  --backdrop:#d9dadc;
  --rule:#9aa0a8;
  --faint:#eef0f3;
}
*{box-sizing:border-box;margin:0;padding:0}
html,body{width:1200px;height:454px;overflow:hidden}
body{background:var(--backdrop);position:relative;font-family:'Lato',Arial,sans-serif;color:var(--ink)}
.piece{position:absolute;background:var(--paper);box-shadow:0 2px 6px rgba(0,0,0,.18);overflow:hidden}
.band{position:absolute;right:0;bottom:0;width:100%;height:auto;display:block}

/* brand lockup */
.brand{position:absolute;display:flex;align-items:center;gap:5px}
.brand-mark{width:9px;height:9px;background:var(--navy);flex:none}
.brand-name{font-family:'Cormorant Garamond',Georgia,serif;font-weight:600;color:var(--navy);letter-spacing:.04em;line-height:1;white-space:nowrap}
.brand.on-dark .brand-mark{background:#fff}
.brand.on-dark .brand-name{color:#fff}
.watermark{position:absolute;left:0;right:0;text-align:center;font-family:'Cormorant Garamond',Georgia,serif;font-weight:600;color:var(--faint);letter-spacing:.06em}

.contact{position:absolute;font-style:normal;font-size:4.6px;line-height:1.45;color:var(--muted);white-space:nowrap}

/* business cards */
.card{left:31px;width:130px;height:72px}
.card-front{top:163px}
.card-front .brand{left:7px;top:11px;gap:3px}
.card-front .brand-mark{width:6px;height:6px}
.card-front .brand-name{font-size:6px}
.card-front .person{position:absolute;left:68px;top:9px;font-size:4.6px;font-weight:700;color:var(--ink);white-space:nowrap}
.card-front .role{position:absolute;left:68px;top:15px;font-size:3.6px;color:var(--muted)}
.card-front .contact{left:68px;top:22px;font-size:3.2px}
.card-back{top:245px;background:var(--navy)}
.card-back .brand{left:0;right:0;top:30px;justify-content:center}
.card-back .brand-name{font-size:11px}

/* letterhead */
.letterhead{left:180px;top:22px;width:316px;height:410px}
.sheet-brand{left:18px;top:18px}
.sheet-brand .brand-name{font-size:13px}
.letterhead .contact,.fax .contact{left:188px;top:16px}
.watermark.sheet{top:180px;font-size:40px}

/* fax */
.fax{left:516px;top:22px;width:316px;height:410px}
.fax-title{position:absolute;left:18px;top:66px;font-size:9px;font-weight:300;letter-spacing:.08em;color:var(--ink)}
.fax-table{position:absolute;left:18px;top:82px;width:190px;border-collapse:collapse;font-size:4.6px;color:var(--ink)}
.fax-table td{border:.6px solid var(--rule);height:10px;padding:0 3px;width:25%}
.fax-table td.label{color:var(--muted)}
.fax-checks{position:absolute;left:18px;top:148px;display:flex;gap:12px;font-size:4.4px;color:var(--muted)}
.fax-checks span::before{content:"";display:inline-block;width:4px;height:4px;border:.6px solid var(--rule);margin-right:2px;vertical-align:-1px}

/* envelopes */
.envelope{left:868px;width:308px;height:138px}
.envelope-front{top:108px}
.envelope-front .brand{left:14px;top:14px}
.envelope-front .brand-name{font-size:11px}
.envelope-back{top:270px;background:var(--navy)}
.flap{position:absolute;inset:0;width:100%;height:100%}
.envelope-back .brand{left:0;right:0;top:64px;justify-content:center}
.envelope-back .brand-name{font-size:12px}
</style>
</head>
<body>

<svg width="0" height="0" style="position:absolute" aria-hidden="true">
  <defs>
    <symbol id="corner-band" viewBox="0 0 300 20" preserveAspectRatio="none">
      <path d="M130 20 C150 8 170 4 200 3 L300 0 L300 20 Z" fill="#1c3f7a"/>
      <path d="M128 20 C148 6 170 1 200 0.5 L300 -2" fill="none" stroke="#111" stroke-width="1"/>
    </symbol>
  </defs>
</svg>

<!-- Business card front -->
<section class="piece card card-front" aria-label="Business card, front">
  <div class="brand"><span class="brand-mark"></span><span class="brand-name">HALVORSEN</span></div>
  <p class="person">Thomas R. Halvorsen</p>
  <p class="role">Attorney At Law</p>
  <address class="contact">Two Cedar Court<br>247 N.W. Ninth Street, Suite 2306<br>Fort Lauderdale, FL 33271<br>T 954.555.0142<br>thomas@halvorsenlegalgroup.com<br>www.halvorsenlegalgroup.com</address>
  <svg class="band" viewBox="0 0 300 20" preserveAspectRatio="none" style="height:9px"><use href="#corner-band"/></svg>
</section>

<!-- Business card back -->
<section class="piece card card-back" aria-label="Business card, back">
  <div class="brand on-dark"><span class="brand-mark"></span><span class="brand-name">HALVORSEN</span></div>
</section>

<!-- Letterhead -->
<section class="piece letterhead" aria-label="Letterhead">
  <div class="brand sheet-brand"><span class="brand-mark"></span><span class="brand-name">HALVORSEN</span></div>
  <address class="contact">Two Cedar Court<br>247 N.W. Ninth Street, Suite 2306<br>Fort Lauderdale, FL 33271<br>T 954.555.0142<br>F 954.555.0143<br>thomas@halvorsenlegalgroup.com<br>www.halvorsenlegalgroup.com</address>
  <p class="watermark sheet" aria-hidden="true">HALVORSEN</p>
  <svg class="band" viewBox="0 0 300 20" preserveAspectRatio="none" style="height:16px"><use href="#corner-band"/></svg>
</section>

<!-- Fax cover -->
<section class="piece fax" aria-label="Fax cover sheet">
  <div class="brand sheet-brand"><span class="brand-mark"></span><span class="brand-name">HALVORSEN</span></div>
  <address class="contact">Two Cedar Court<br>247 N.W. Ninth Street, Suite 2306<br>Fort Lauderdale, FL 33271<br>T 954.555.0142<br>F 954.555.0143<br>thomas@halvorsenlegalgroup.com<br>www.halvorsenlegalgroup.com</address>
  <h1 class="fax-title">FAX</h1>
  <table class="fax-table">
    <tr><td class="label">To:</td><td></td><td class="label">From:</td><td></td></tr>
    <tr><td class="label">Company:</td><td></td><td class="label">Phone:</td><td></td></tr>
    <tr><td class="label">Fax:</td><td></td><td class="label">Date:</td><td></td></tr>
    <tr><td class="label">Re:</td><td></td><td class="label">No. of Pages:</td><td></td></tr>
    <tr><td class="label">CC:</td><td colspan="3"></td></tr>
  </table>
  <div class="fax-checks"><span>Urgent</span><span>For Review</span><span>Please Reply</span><span>Please Recycle</span></div>
  <p class="watermark sheet" aria-hidden="true">HALVORSEN</p>
  <svg class="band" viewBox="0 0 300 20" preserveAspectRatio="none" style="height:16px"><use href="#corner-band"/></svg>
</section>

<!-- Envelope front -->
<section class="piece envelope envelope-front" aria-label="Envelope, front">
  <div class="brand"><span class="brand-mark"></span><span class="brand-name">HALVORSEN</span></div>
  <svg class="band" viewBox="0 0 300 20" preserveAspectRatio="none" style="height:12px"><use href="#corner-band"/></svg>
</section>

<!-- Envelope back -->
<section class="piece envelope envelope-back" aria-label="Envelope, back">
  <svg class="flap" viewBox="0 0 308 138" preserveAspectRatio="none" aria-hidden="true">
    <path d="M0 0 L154 80 L308 0 Z" fill="#14305f"/>
    <path d="M0 0 L154 80 L308 0" fill="none" stroke="#0e2245" stroke-width="1"/>
    <path d="M0 138 L120 62 M308 138 L188 62" stroke="#2a4f8c" stroke-width="1"/>
  </svg>
  <div class="brand on-dark"><span class="brand-mark"></span><span class="brand-name">HALVORSEN</span></div>
</section>

</body>
</html>
```